Deactivated Coal-Fired Power Plant to be redeveloped into a Green Energy Campus.

Want a striking business card statement that introduces our concept project to provide economic and community recovery to a former rural coal community in western PA.
Essentially 12 project representatives that will lead both the demolition of an existing power plant and the redevelopment to a new Green energy site.
Business Card should reflect our effort.
We are open to ideas.

Target Market(s)

Energy and Power Generation industries

Industry/Entity Type

Power Generation and Data Centers

Contact Information for Business Card

Included in uploaded materials

Font styles to use
Sans Serif
Other font styles liked:
• Arial, Calibri

Requirements
Must have
• Multiple colors

```html
<!DOCTYPE html>
<html lang="en">
<head>
<meta charset="utf-8">
<title>Ridgeline Renewal – Business Cards</title>
<link href="https://fonts.googleapis.com/css2?family=Montserrat:wght@500;600;700&display=swap" rel="stylesheet">
<style>
  :root {
    --green: #1a9a4c;
    --ink: #1d1d1b;
    --paper: #ffffff;
    --night: #070707;
    --stage: #3a3a3a;
    --photo-sky: #8fa08a;
    --photo-field: #4f7a3c;
    --photo-dark: #2f4a2a;
  }
  * { box-sizing: border-box; margin: 0; padding: 0; }
  html, body { width: 1200px; height: 900px; overflow: hidden; }
  body {
    background: var(--stage);
    font-family: "Montserrat", Arial, sans-serif;
    position: relative;
  }
  .card {
    position: absolute;
    width: 514px;
    height: 296px;
    box-shadow: 0 6px 18px rgba(0,0,0,.45);
    overflow: hidden;
  }
  .card--front { left: 343px; top: 138px; background: var(--paper); }
  .card--photo { left: 72px; top: 464px; }
  .card--dark { left: 615px; top: 464px; background: var(--night); }

  .brand {
    display: flex; align-items: center; gap: 10px;
    font-weight: 700; letter-spacing: .5px; text-transform: uppercase;
  }
  .brand__dot { border-radius: 50%; background: var(--green); flex: none; }

  .card--front .brand {
    position: absolute; right: 34px; top: 96px;
    font-size: 19px; color: var(--ink);
  }
  .card--front .brand__dot { width: 22px; height: 22px; }

  .contact { position: absolute; left: 39px; top: 164px; }
  .contact__name { color: var(--green); font-weight: 600; font-size: 17px; letter-spacing: .6px; }
  .contact__role { color: var(--ink); font-weight: 600; font-size: 11.5px; letter-spacing: .4px; margin-top: 4px; }
  .contact__rule { width: 53px; height: 2px; background: var(--green); margin: 12px 0 12px; }
  .contact__line { font-size: 13.5px; font-weight: 500; color: var(--ink); line-height: 17.5px; }
  .contact__key { color: var(--green); display: inline-block; width: 16px; }

  .photo-fill {
    position: absolute; inset: 0;
    background: linear-gradient(175deg, var(--photo-sky) 0%, var(--photo-field) 35%, var(--photo-dark) 70%, var(--photo-field) 100%);
  }
  .centered {
    position: absolute; left: 0; right: 0;
    display: flex; justify-content: center;
  }
  .card--photo .brand, .card--dark .brand { font-size: 27px; }
  .card--photo .brand { color: #fff; }
  .card--dark .brand { color: #fff; }
  .card--photo .brand__dot, .card--dark .brand__dot { width: 30px; height: 30px; }
  .brand-row { top: 128px; }
  .web {
    font-size: 13px; font-weight: 600; color: #fff; letter-spacing: .2px;
  }
  .card--photo .web { position: absolute; left: 143px; top: 264px; }
  .card--dark .web-row { top: 264px; }
  .web__domain { color: var(--green); }
</style>
</head>
<body>
  <section class="card card--front">
    <div class="brand"><span class="brand__dot"></span>Ridgeline Renewal</div>
    <div class="contact">
      <p class="contact__name">DANIEL OKAFOR</p>
      <p class="contact__role">CHIEF OPERATING OFFICER</p>
      <div class="contact__rule"></div>
      <p class="contact__line"><span class="contact__key">P</span>555 010 2400</p>
      <p class="contact__line"><span class="contact__key">M</span>555 010 2400</p>
      <p class="contact__line"><span class="contact__key">E</span>dokafor@ridgelinerenewal.com</p>
    </div>
  </section>

  <section class="card card--photo">
    <div class="photo-fill" role="img" aria-label="Aerial photograph of the former power plant site among green rural fields"></div>
    <div class="centered brand-row"><div class="brand"><span class="brand__dot"></span>Ridgeline Renewal</div></div>
    <p class="web">www.ridgelinerenewal.com</p>
  </section>

  <section class="card card--dark">
    <div class="centered brand-row"><div class="brand"><span class="brand__dot"></span>Ridgeline Renewal</div></div>
    <div class="centered web-row"><p class="web">www.<span class="web__domain">ridgelinerenewal</span>.com</p></div>
  </section>
</body>
</html>
```